New Dental Office Needs an Attractive and user friendly Website Designed

I need a website for a new dental office. The Name is Maplecrest Dentistry. I would like a Modern design with a user friendly interface and usability.
I would like a landing page, a page that lists the services we offer: Cosmetic Dentistry, Implants, Dental Hygiene, Emergency Services, Restorations, Dentures
Target Market(s)
Mid to upper class
Industry/Entity Type
Dentistry
Coding
Coded - Design and coding required
Number of Pages Required
1 page
Requirements
Must have
- Landing page that has a scheduling option, Procedures, operating hours, and contact us info
Nice to have
- Appealing design, Soft comforting colors. Easy to navigate page, Modern and professional.

```html
<!DOCTYPE html>
<html lang="en">
<head>
<meta charset="utf-8">
<title>Maplecrest Dentistry</title>
<link href="https://fonts.googleapis.com/css2?family=Libre+Baskerville:ital,wght@0,400;0,700;1,400&family=Poppins:ital,wght@0,400;0,500;0,600;1,400&display=swap" rel="stylesheet">
<style>
:root{
  --ink:#1f1d1b;
  --dark:#262422;
  --gold:#e8d48e;
  --gold-deep:#cfb766;
  --mist:#f6f5f3;
  --cream:#f3f0ea;
  --white:#ffffff;
  --muted:#555049;
}
*{box-sizing:border-box;margin:0;padding:0}
html,body{width:1200px;height:4474px;overflow:hidden}
body{position:relative;background:var(--white);font-family:"Poppins",sans-serif;color:var(--ink)}
.serif{font-family:"Libre Baskerville",serif}
.abs{position:absolute}

/* nav */
.site-nav{left:0;top:0;width:1200px;height:83px;background:var(--dark);display:flex;align-items:center}
.nav-link{position:absolute;top:35px;color:var(--white);font-size:13px;letter-spacing:.3px;text-decoration:none}
.brand{position:absolute;left:0;width:1200px;text-align:center;top:28px;font-family:"Libre Baskerville",serif;font-size:21px;color:var(--white)}

/* hero */
.hero{left:0;top:83px;width:1200px;height:622px;background:linear-gradient(100deg,#9aa3a6 0%,#b9c0c0 35%,#cfd3cf 60%,#7f9a86 100%)}
.hero-shade{left:0;top:83px;width:1200px;height:622px;background:linear-gradient(90deg,rgba(30,30,30,.45),rgba(30,30,30,.1) 60%,rgba(0,0,0,0))}
.hero-title{left:127px;top:250px;font-size:66px;line-height:74px;color:var(--white);font-weight:700}
.hero-rule{left:428px;top:364px;width:85px;height:2px;background:var(--white)}
.btn{position:absolute;height:42px;border-radius:21px;display:flex;align-items:center;justify-content:center;font-size:13.5px;font-weight:600;letter-spacing:.2px}
.btn-gold{background:var(--gold);color:var(--ink)}
.btn-dark{background:var(--dark);color:var(--white)}

/* waves */
.wave{left:0;width:1200px}

/* about */
.photo{position:absolute}
.about-heading{left:560px;top:828px;font-size:42px;line-height:42px;font-weight:700}
.about-copy{left:695px;top:960px;width:385px;font-size:14.5px;line-height:24px;color:var(--ink)}

.section-title{position:absolute;left:0;width:1200px;text-align:center;font-family:"Libre Baskerville",serif;font-weight:700;font-size:42px}

/* services */
.service{position:absolute;width:457px;height:155px;border-radius:78px;background:var(--white);box-shadow:0 6px 22px rgba(0,0,0,.07)}
.service .icon{position:absolute;top:20px;width:115px;height:115px;border-radius:50%;background:var(--cream);display:flex;align-items:center;justify-content:center}
.service h3{position:absolute;top:35px;font-size:19px;font-weight:600}
.service p{position:absolute;top:70px;width:240px;font-size:13px;line-height:19px;color:var(--muted)}
.service.left .icon{right:20px}
.service.left h3,.service.left p{right:146px;text-align:right}
.service.right .icon{left:20px}
.service.right h3,.service.right p{left:146px;text-align:left}

/* team */
.member{position:absolute;border-radius:6px;box-shadow:0 4px 14px rgba(0,0,0,.08)}
.name-pill{left:516px;top:2576px;width:167px;height:35px;border-radius:18px;background:var(--gold);font-size:16px;font-weight:500;display:flex;align-items:center;justify-content:center}
.role{left:0;width:1200px;top:2620px;text-align:center;font-size:13.5px;font-weight:500}

/* testimonial */
.stars{left:0;width:1200px;top:2918px;text-align:center;color:var(--gold-deep);font-size:22px;letter-spacing:2px}
.quote{left:250px;width:700px;top:2955px;text-align:center;font-style:italic;font-size:19px;line-height:30px}
.quote-name{left:0;width:1200px;top:3020px;text-align:center;font-weight:600;font-size:18px}
.arrow{position:absolute;top:2955px;width:32px;height:32px}

/* procedures */
.proc{position:absolute;top:3255px;height:320px;border-radius:6px}
.proc-name{position:absolute;top:3597px;width:273px;text-align:center;font-family:"Libre Baskerville",serif;font-weight:700;font-size:17px}

/* cta */
.cta{left:0;top:3714px;width:1200px;height:380px;background:linear-gradient(110deg,#3b3733,#56504a 45%,#3a3632)}
.cta-eyebrow{left:0;width:1200px;top:3818px;text-align:center;color:var(--white);font-size:19px;letter-spacing:.3px}
.cta-title{left:0;width:1200px;top:3858px;text-align:center;color:var(--white);font-size:38px;font-weight:700}

/* footer */
.footer{left:0;top:4126px;width:1200px;height:348px;background:var(--dark);color:var(--white)}
.footer-brand{left:127px;top:4172px;font-family:"Libre Baskerville",serif;font-size:28px;color:var(--white)}
.social{position:absolute;top:4273px;width:24px;height:24px;border-radius:50%;border:2px solid var(--white)}
.copyright{left:144px;top:4350px;font-size:13px;color:var(--white)}
.footer-head{position:absolute;top:4180px;font-family:"Libre Baskerville",serif;font-weight:700;font-size:19px;color:var(--white)}
.hours{left:441px;top:4228px;font-size:13px;line-height:25px;color:var(--white)}
.hours span{display:inline-block;width:115px}
.contact-icon{position:absolute;left:796px;width:36px;height:36px;border-radius:50%;background:var(--gold);display:flex;align-items:center;justify-content:center}
.contact-text{position:absolute;left:848px;font-size:13px;line-height:20px;color:var(--white)}
.request{left:848px;top:4352px;font-size:13px;color:var(--gold);text-decoration:underline}
</style>
</head>
<body>

<header class="abs site-nav">
  <a class="nav-link" style="left:127px">HOME</a>
  <a class="nav-link" style="left:213px">ABOUT US</a>
  <a class="nav-link" style="left:333px">OUR SERVICES</a>
  <div class="brand">Maplecrest Dentistry</div>
  <a class="nav-link" style="left:763px">OUR TEAM</a>
  <a class="nav-link" style="left:881px">BLOG</a>
  <a class="nav-link" style="left:967px">BOOK AN APPT.</a>
</header>

<section>
  <div class="abs hero" role="img" aria-label="Dentist in mask treating a smiling patient in a bright clinic"></div>
  <div class="abs hero-shade"></div>
  <h1 class="abs hero-title serif">Maplecrest<br>Dentistry</h1>
  <div class="abs hero-rule"></div>
  <a class="btn btn-gold" style="left:127px;top:424px;width:275px">BOOK YOUR APPOINTMENT</a>
</section>

<svg class="abs wave" style="top:1180px" width="1200" height="420" viewBox="0 0 1200 420" aria-hidden="true">
  <path d="M0 80 C200 20 330 120 520 160 C720 200 820 60 1000 50 C1100 45 1160 80 1200 100 L1200 420 L0 420 Z" fill="#f7f6f4"/>
</svg>

<section>
  <div class="photo" style="left:127px;top:816px;width:307px;height:429px;background:linear-gradient(160deg,#d8dcda,#8faaa2 55%,#4c6a62)" role="img" aria-label="Dental hygienist treating a reclining patient"></div>
  <div class="photo" style="left:457px;top:1020px;width:191px;height:241px;border-radius:0 95px 0 0;background:linear-gradient(180deg,#cfc8c2,#b8a29a 45%,#d994b4)" role="img" aria-label="Smiling young woman pointing at her teeth"></div>
  <h2 class="abs about-heading serif">About Maplecrest<br>Dentistry</h2>
  <p class="abs about-copy">Lorem ipsum dolor sit amet, consectetur adi piscing elit, sed do eiusmod tempor incid idunt ut labore et dolore magna aliqua. Quis ipsum suspendisse ultrices gravida. Risus commodo viverra maecenas accumsan lacusLorem ipsum dolor sit amet, consectetur adi piscing elit, sed do eiusmod tempor incid idunt ut labore et dolore magna aliqua. Quis ipsum suspendisse ultrices gravida. Risus commodo.</p>
  <a class="btn btn-dark" style="left:695px;top:1212px;width:274px">BOOK YOUR APPOINTMENT</a>
</section>

<section>
  <h2 class="section-title" style="top:1532px">Services We Offed</h2>

  <div class="service left" style="left:127px;top:1612px">
    <h3>Cosmetic Dentistry</h3>
    <p>Lorem ipsum dolor sit amet, cons ectetur adipiscing elit, sed do eius magna aliqua suspen.</p>
    <div class="icon"><svg width="60" height="60" viewBox="0 0 60 60" fill="none" stroke="#1f1d1b" stroke-width="2"><path d="M18 12c-6 0-9 6-8 13 1 6 3 9 4 16 1 6 3 10 6 10 3 0 3-8 5-12 1-3 4-3 5 0 2 4 2 12 5 12 3 0 5-4 6-10 1-7 3-10 4-16 1-7-2-13-8-13-5 0-7 3-10 3s-5-3-9-3z"/><path d="M47 44l2 4 4 2-4 2-2 4-2-4-4-2 4-2z"/></svg></div>
  </div>
  <div class="service right" style="left:611px;top:1612px">
    <div class="icon"><svg width="60" height="60" viewBox="0 0 60 60" fill="none" stroke="#1f1d1b" stroke-width="2"><path d="M16 16c-6 0-9 6-8 13 1 6 3 9 4 16 1 5 3 9 6 9 3 0 3-8 5-12 1-3 4-3 5 0 2 4 2 12 5 12 3 0 5-4 6-9 1-6 2-9 3-13"/><path d="M40 8h6v6h6v6h-6v6h-6v-6h-6v-6h6z"/></svg></div>
    <h3>Emergency Services</h3>
    <p>Lorem ipsum dolor sit amet, cons ectetur adipiscing elit, sed do eius magna aliqua suspen.</p>
  </div>

  <div class="service left" style="left:127px;top:1780px">
    <h3>Implants</h3>
    <p>Lorem ipsum dolor sit amet, cons ectetur adipiscing elit, sed do eius magna aliqua suspen.</p>
    <div class="icon"><svg width="60" height="60" viewBox="0 0 60 60" fill="none" stroke="#1f1d1b" stroke-width="2"><path d="M22 8c-4 0-6 3-5 7 1 3 5 4 8 4h10c3 0 7-1 8-4 1-4-1-7-5-7-3 0-5 2-8 2s-5-2-8-2z"/><path d="M24 24h12M25 29h10M26 34h8M27 39h6M30 44v6"/><path d="M10 52h40"/></svg></div>
  </div>
  <div class="service right" style="left:611px;top:1780px">
    <div class="icon"><svg width="60" height="60" viewBox="0 0 60 60" fill="none" stroke="#1f1d1b" stroke-width="2"><path d="M8 34c0-4 4-5 7-4 2 1 4 1 6 0 3-1 7 0 7 4 0 5-2 8-3 14 0 2-2 3-3 0l-2-6-2 6c-1 3-3 2-3 0-1-6-3-9-3-14z"/><path d="M32 34c0-4 4-5 7-4 2 1 4 1 6 0 3-1 7 0 7 4 0 5-2 8-3 14 0 2-2 3-3 0l-2-6-2 6c-1 3-3 2-3 0-1-6-3-9-3-14z"/><path d="M26 10c-3 0-4 3-3 5s3 3 5 3h4c2 0 4-1 5-3s0-5-3-5c-2 0-3 1-4 1s-2-1-4-1zM30 18v10"/></svg></div>
    <h3>Restorations</h3>
    <p>Lorem ipsum dolor sit amet, cons ectetur adipiscing elit, sed do eius magna aliqua suspen.</p>
  </div>

  <div class="service left" style="left:127px;top:1950px">
    <h3>Dental Hygiene</h3>
    <p>Lorem ipsum dolor sit amet, cons ectetur adipiscing elit, sed do eius magna aliqua suspen.</p>
    <div class="icon"><svg width="60" height="60" viewBox="0 0 60 60" fill="none" stroke="#1f1d1b" stroke-width="2"><path d="M18 12c-6 0-9 6-8 13 1 6 3 9 4 16 1 6 3 10 6 10 3 0 3-8 5-12 1-3 4-3 5 0 2 4 2 12 5 12 3 0 5-4 6-10 1-7 3-10 4-16 1-7-2-13-8-13-5 0-7 3-10 3s-5-3-9-3z"/><path d="M11 26c6 3 12 4 19 4s13-1 19-4"/></svg></div>
  </div>
  <div class="service right" style="left:611px;top:1950px">
    <div class="icon"><svg width="64" height="60" viewBox="0 0 64 60" fill="none" stroke="#1f1d1b" stroke-width="2"><rect x="6" y="12" width="52" height="36" rx="10"/><path d="M12 24h40M12 36h40M20 18v6M28 18v6M36 18v6M44 18v6M20 36v6M28 36v6M36 36v6M44 36v6"/></svg></div>
    <h3>Dentures</h3>
    <p>Lorem ipsum dolor sit amet, cons ectetur adipiscing elit, sed do eius magna aliqua suspen.</p>
  </div>
</section>

<section>
  <h2 class="section-title" style="top:2245px">Meet Our Dental Experts</h2>
  <svg class="abs wave" style="top:2480px" width="1200" height="660" viewBox="0 0 1200 660" aria-hidden="true">
    <path d="M0 40 C180 80 320 170 520 190 C760 210 880 110 1060 110 C1130 110 1170 120 1200 130 L1200 560 C1000 640 800 660 600 640 C400 620 200 600 0 560 Z" fill="#f7f6f4"/>
  </svg>
  <div class="member" style="left:127px;top:2355px;width:162px;height:181px;background:linear-gradient(180deg,#eef0f0,#d9dcdc)" role="img" aria-label="Portrait of smiling female dentist in white coat"></div>
  <div class="member" style="left:314px;top:2355px;width:162px;height:181px;background:linear-gradient(180deg,#e6ebee,#2d5a80 70%)" role="img" aria-label="Portrait of male dentist in blue scrubs"></div>
  <div class="member" style="left:500px;top:2336px;width:202px;height:221px;background:linear-gradient(180deg,#f0f2f3,#c9d3da)" role="img" aria-label="Portrait of female dentist wearing a mask"></div>
  <div class="member" style="left:723px;top:2355px;width:162px;height:181px;background:linear-gradient(180deg,#eef0f0,#dfe2e2)" role="img" aria-label="Portrait of smiling female dentist with arms crossed"></div>
  <div class="member" style="left:910px;top:2355px;width:162px;height:181px;background:linear-gradient(180deg,#eef1f3,#c7d6e0)" role="img" aria-label="Portrait of smiling male dentist in white coat"></div>
  <div class="abs name-pill">Doctor Name</div>
  <div class="abs role">Cosmetic Dentistry</div>
</section>

<section>
  <h2 class="section-title" style="top:2838px">Our Patients Have to Say</h2>
  <div class="abs stars">★★★★★</div>
  <svg class="arrow" style="left:193px" viewBox="0 0 32 32" fill="none" stroke="#1f1d1b" stroke-width="1.6"><circle cx="16" cy="16" r="14.5"/><path d="M18 10l-6 6 6 6"/></svg>
  <p class="abs quote">Lorem ipsum dolor sit amet, consectetur adipiscing elit, sed do eius mod tempor incididunt ut labore et dolore magna aliqua.</p>
  <svg class="arrow" style="left:993px" viewBox="0 0 32 32" fill="none" stroke="#1f1d1b" stroke-width="1.6"><circle cx="16" cy="16" r="14.5"/><path d="M14 10l6 6-6 6"/></svg>
  <div class="abs quote-name">Clara Whitfield</div>
</section>

<section>
  <h2 class="section-title" style="top:3176px">Procedures</h2>
  <div class="proc" style="left:127px;width:273px;background:linear-gradient(160deg,#c9d0cd,#d9b9a4 50%,#4a78c4)" role="img" aria-label="Patient smiling during a dental check-up"></div>
  <div class="proc" style="left:431px;width:273px;background:linear-gradient(160deg,#e7e9ea,#b5c3cc 50%,#3f74c2)" role="img" aria-label="Dentist examining a smiling patient"></div>
  <div class="proc" style="left:735px;width:273px;background:linear-gradient(160deg,#b4967d,#d7b7a1 50%,#e6e2de)" role="img" aria-label="Close-up of a patient's smile with dental tools"></div>
  <div class="proc" style="left:1032px;width:168px;border-radius:6px 0 0 6px;background:linear-gradient(160deg,#c6cfd6,#d8b8a8 60%,#a0908a)" role="img" aria-label="Hands holding a denture model"></div>
  <div class="proc-name" style="left:127px">Procedure Name</div>
  <div class="proc-name" style="left:431px">Procedure Name</div>
  <div class="proc-name" style="left:735px">Procedure Name</div>
</section>

<section>
  <div class="abs cta" role="img" aria-label="Dimmed photo of a dentist treating a patient"></div>
  <div class="abs cta-eyebrow">READY FOR A SMILE YOU'LL LOVE?</div>
  <h2 class="abs cta-title serif">Schedule Your First Appointment</h2>
  <a class="btn btn-gold" style="left:464px;top:3924px;width:273px">BOOK YOUR APPOINTMENT</a>
</section>

<footer>
  <div class="abs footer"></div>
  <div class="abs footer-brand">Maplecrest Dentistry</div>
  <div class="social" style="left:202px" aria-label="Social profile"></div>
  <div class="social" style="left:252px" aria-label="Social profile"></div>
  <div class="abs copyright">© 2025 All rights reserved.</div>

  <div class="footer-head" style="left:441px">Operating Hours</div>
  <div class="abs hours">
    <div><span>Monday:</span>08:00 am - 05:00 pm</div>
    <div><span>Tuesday:</span>08:00 am - 05:00 pm</div>
    <div><span>Wednesday:</span>08:00 am - 05:00 pm</div>
    <div><span>Thursday:</span>08:00 am - 05:00 pm</div>
    <div><span>Friday:</span>08:00 am - 05:00 pm</div>
    <div><span>Saturday:</span>Closed</div>
    <div><span>Sunday:</span>Closed</div>
  </div>

  <div class="footer-head" style="left:796px">Contact Us</div>
  <div class="contact-icon" style="top:4230px"><svg width="18" height="18" viewBox="0 0 24 24" fill="none" stroke="#1f1d1b" stroke-width="2"><path d="M12 22s7-7 7-12a7 7 0 0 0-14 0c0 5 7 12 7 12z"/><circle cx="12" cy="10" r="2.5"/></svg></div>
  <div class="contact-text" style="top:4228px">Maplecrest Dentistry<br>88 Orchard Row, Sample City SK</div>
  <div class="contact-icon" style="top:4292px"><svg width="18" height="18" viewBox="0 0 24 24" fill="none" stroke="#1f1d1b" stroke-width="2"><path d="M5 3h4l2 5-3 2a12 12 0 0 0 6 6l2-3 5 2v4a2 2 0 0 1-2 2A18 18 0 0 1 3 5a2 2 0 0 1 2-2z"/></svg></div>
  <div class="contact-text" style="top:4290px">Phone<br>(555) 014-2278</div>
  <a class="abs request">REQUEST APPOINTMENT</a>
</footer>

</body>
</html>
```